Redesign of business card for Birchline Mechanical

We are looking for a new design for our business cards for Birchline Mechanical. We are a plumbing & HVAC construction company, operating on the West Coast of Canada and USA. Logo attached.
Industry/Entity Type
Construction - Plumbing & HVAC
Contact Information for Business Card
Name, address, phone numbers, email, website address
Look and feel
Each slider illustrates characteristics of the customer's brand and the style your logo design should communicate.

```html
<!DOCTYPE html>
<html lang="en">
<head>
<meta charset="utf-8">
<title>Birchline Mechanical – Business Card</title>
<link href="https://fonts.googleapis.com/css2?family=Barlow+Condensed:wght@400;500;700&display=swap" rel="stylesheet">
<style>
  :root {
    --ink: #111111;
    --paper: #ffffff;
    --backdrop: #efefef;
    --muted: #222222;
  }
  * { box-sizing: border-box; margin: 0; padding: 0; }
  html, body {
    width: 1102px; height: 1200px; overflow: hidden;
    background: var(--backdrop);
    font-family: "Barlow Condensed", "Arial Narrow", sans-serif;
    color: var(--ink);
  }
  .canvas { position: relative; width: 1102px; height: 1200px; }

  /* Front of card */
  .card-front {
    position: absolute; left: 176px; top: 123px;
    width: 764px; height: 436px;
    border-radius: 14px; overflow: hidden;
    background: var(--ink);
  }
  .card-front__pattern {
    position: absolute; inset: 0;
    background: radial-gradient(ellipse at 50% 45%, #2a2a2a 0%, #161616 45%, #0b0b0b 100%);
  }
  .card-front__brand {
    position: absolute; left: 0; right: 0; top: 190px;
    text-align: center;
    display: flex; align-items: center; justify-content: center; gap: 16px;
    color: var(--paper);
    font-weight: 700; font-size: 40px; letter-spacing: 2px; text-transform: uppercase;
  }
  .brand-square { width: 26px; height: 26px; border: 4px solid currentColor; }

  /* Back of card */
  .card-back {
    position: absolute; left: 174px; top: 631px;
    width: 766px; height: 436px;
    border-radius: 14px;
    background: var(--ink);
  }
  .card-back__gap {
    position: absolute; width: 10px; height: 18px; background: var(--backdrop);
  }
  .card-back__gap--top { top: 0; }
  .card-back__gap--bottom { bottom: 0; }
  .card-back__panel {
    position: absolute; left: 18px; top: 18px; right: 18px; bottom: 18px;
    background: var(--paper); border-radius: 12px;
  }
  .holder-name {
    position: absolute; left: 50px; top: 46px;
    font-weight: 700; font-size: 36px; letter-spacing: 2px; line-height: 1;
  }
  .holder-title {
    position: absolute; left: 50px; top: 89px;
    font-size: 20px; letter-spacing: 1.5px; color: var(--muted); line-height: 1;
  }
  .address {
    position: absolute; left: 544px; top: 58px;
    display: flex; align-items: center; gap: 14px;
    font-size: 20px; letter-spacing: 1.5px; line-height: 1;
  }
  .contact-list { position: absolute; left: 50px; top: 228px; list-style: none; }
  .contact-list li {
    display: flex; align-items: center; gap: 14px;
    height: 46px; font-size: 21px; letter-spacing: 1.5px;
  }
  .contact-list svg { width: 22px; height: 22px; flex: none; }
  .card-back__brand {
    position: absolute; left: 470px; top: 340px; width: 262px;
    display: flex; align-items: center; gap: 10px; justify-content: flex-end;
    font-weight: 700; font-size: 22px; letter-spacing: 1px; text-transform: uppercase;
  }
  .card-back__brand .brand-square { width: 18px; height: 18px; border-width: 3px; }
</style>
</head>
<body>
<main class="canvas">
  <section class="card-front">
    <div class="card-front__pattern" role="img" aria-label="Dark background with concentric outline pattern"></div>
    <div class="card-front__brand"><span class="brand-square"></span>Birchline Mechanical</div>
  </section>

  <section class="card-back">
    <span class="card-back__gap card-back__gap--top" style="left:42px"></span>
    <span class="card-back__gap card-back__gap--top" style="left:575px"></span>
    <span class="card-back__gap card-back__gap--bottom" style="left:218px"></span>
    <span class="card-back__gap card-back__gap--bottom" style="left:717px"></span>
    <div class="card-back__panel"></div>

    <h1 class="holder-name">YOUR FULL NAME</h1>
    <p class="holder-title">TITLE</p>

    <p class="address">
      <svg width="22" height="30" viewBox="0 0 22 30" fill="none" stroke="currentColor" stroke-width="2.2">
        <path d="M11 28 C11 28 2 17 2 10.5 A9 9 0 0 1 20 10.5 C20 17 11 28 11 28 Z"/>
        <circle cx="11" cy="10.5" r="3.3"/>
      </svg>
      YOUR ADDRESS
    </p>

    <ul class="contact-list">
      <li>
        <svg viewBox="0 0 24 24" fill="none" stroke="currentColor" stroke-width="1.8"><rect x="6" y="1.5" width="12" height="21" rx="1.5"/><line x1="11" y1="19" x2="13" y2="19"/></svg>
        123 4567 8900
      </li>
      <li>
        <svg viewBox="0 0 24 24" fill="none" stroke="currentColor" stroke-width="1.8"><path d="M6 2.5 L9.5 7 L7.5 9.5 C9 13 11 15 14.5 16.5 L17 14.5 L21.5 18 L19 21.5 C11 21 3 13 2.5 5 Z" stroke-linejoin="round"/></svg>
        123 4567 8900
      </li>
      <li>
        <svg viewBox="0 0 24 24" fill="none" stroke="currentColor" stroke-width="1.8"><rect x="2" y="5" width="20" height="14"/><path d="M2 5 L12 13 L22 5 M2 19 L9.5 11 M22 19 L14.5 11"/></svg>
        your@email.com
      </li>
      <li>
        <svg viewBox="0 0 24 24" fill="none" stroke="currentColor" stroke-width="1.8"><circle cx="12" cy="12" r="10"/><ellipse cx="12" cy="12" rx="4.5" ry="10"/><line x1="2" y1="12" x2="22" y2="12"/></svg>
        www.websitelink.com
      </li>
    </ul>

    <div class="card-back__brand"><span class="brand-square"></span>Birchline Mechanical</div>
  </section>
</main>
</body>
</html>
```